Would like a design for lawn signs I will be using to advertise with. Attached are three images. One is the jpeg version of our logo to use in creating and editing the design. The other two are mock ups of our current style of tshirt and business card design. I would like the finished product to look similar in style to the mock ups. The actual color of our logo in the jpeg picture is outdated coloring. I would like the logo to be the color of the logo in the mock up tshirt version and the business card design.
The signs I will be using are white in color and 18"x24" white lawn signs, so I would like the logo to appear like the logo in the grey tshirt design, where it is black and orange. As for the text coloring I would like it to be black as well.
The only things I want included on the text of the sign design is:
Phone: 816-402-7761
Email: tidyturfco@fernmail.com
Mowing
Fertilization
Aeration
Bed & tree maintenance
and more.

```html
<!DOCTYPE html>
<html lang="en">
<head>
<meta charset="utf-8">
<title>Tidy Turf Co. – Lawn Sign</title>
<link href="https://fonts.googleapis.com/css2?family=Alegreya+Sans:wght@700&family=Open+Sans:wght@400;800&display=swap" rel="stylesheet">
<style>
  :root {
    --paper: #ffffff;
    --ink: #000000;
    --accent: #ff4000;
  }
  html, body {
    margin: 0;
    padding: 0;
    width: 1200px;
    height: 900px;
    overflow: hidden;
    background: var(--paper);
  }
  .sign {
    position: relative;
    width: 1200px;
    height: 900px;
    background: var(--paper);
  }
  .sign-frame {
    position: absolute;
    left: 23px;
    top: 22px;
    width: 1151px;
    height: 854px;
    border: 2px solid var(--ink);
    box-sizing: border-box;
  }
  .contact-band {
    position: absolute;
    left: 0;
    top: 567px;
    width: 1186px;
    height: 331px;
    background: var(--accent);
  }
  .contact-band-frame {
    position: absolute;
    left: 23px;
    top: 0;
    width: 1152px;
    height: 311px;
    border: 2px solid var(--paper);
    border-top: none;
    box-sizing: border-box;
  }
  .brand {
    position: absolute;
    left: 60px;
    top: 230px;
    width: 540px;
    height: 100px;
    display: flex;
    align-items: center;
    justify-content: center;
    gap: 22px;
  }
  .brand-dot {
    width: 56px;
    height: 56px;
    border-radius: 50%;
    background: var(--accent);
    flex: none;
  }
  .brand-name {
    font-family: "Alegreya Sans", sans-serif;
    font-weight: 700;
    font-size: 76px;
    line-height: 1;
    color: var(--ink);
    white-space: nowrap;
  }
  .services {
    position: absolute;
    right: 52px;
    top: 74px;
    margin: 0;
    padding: 0;
    list-style: none;
    text-align: right;
    font-family: "Alegreya Sans", sans-serif;
    font-weight: 700;
    color: var(--ink);
    letter-spacing: 1.5px;
  }
  .services li {
    font-size: 53px;
    line-height: 66px;
    white-space: nowrap;
  }
  .services .service-first { margin-bottom: 14px; }
  .services .service-main { margin-bottom: 66px; }
  .services .service-more {
    font-size: 40px;
    line-height: 58px;
    letter-spacing: 1px;
  }
  .contact-line {
    position: absolute;
    display: flex;
    align-items: center;
    font-family: "Open Sans", sans-serif;
    color: var(--ink);
    white-space: nowrap;
  }
  .contact-phone {
    left: 120px;
    top: 596px;
    font-weight: 800;
    font-size: 104px;
    line-height: 120px;
    letter-spacing: 12px;
  }
  .contact-email {
    left: 118px;
    top: 746px;
    font-weight: 400;
    font-size: 68px;
    line-height: 86px;
    letter-spacing: 1px;
  }
  .contact-icon { flex: none; }
  .contact-phone .contact-icon { margin-right: 58px; }
  .contact-email .contact-icon { margin-right: 54px; }
</style>
</head>
<body>
<main class="sign">
  <div class="sign-frame"></div>

  <div class="brand">
    <span class="brand-dot"></span>
    <span class="brand-name">Tidy Turf Co.</span>
  </div>

  <ul class="services">
    <li class="service-first">Mowing</li>
    <li>Fertilization</li>
    <li class="service-main">Aeration</li>
    <li>Bed &amp; Tree maintenance</li>
    <li class="service-more">and more..</li>
  </ul>

  <div class="contact-band">
    <div class="contact-band-frame"></div>
  </div>

  <div class="contact-line contact-phone">
    <svg class="contact-icon" width="62" height="78" viewBox="0 0 62 78" aria-hidden="true">
      <path d="M6 4 H56 V70 L50 76 H12 L6 70 Z" fill="none" stroke="#000000" stroke-width="6"/>
      <rect x="19" y="21" width="24" height="24" fill="none" stroke="#000000" stroke-width="6"/>
    </svg>
    <span>816-402-7761</span>
  </div>

  <div class="contact-line contact-email">
    <svg class="contact-icon" width="66" height="44" viewBox="0 0 66 44" aria-hidden="true">
      <rect x="3" y="3" width="60" height="38" fill="none" stroke="#000000" stroke-width="5"/>
      <path d="M3 3 L33 24 L63 3 M3 41 L26 19 M63 41 L40 19" fill="none" stroke="#000000" stroke-width="5"/>
    </svg>
    <span>tidyturfco@fernmail.com</span>
  </div>
</main>
</body>
</html>
```